Varnek Group Business Card

Varnek Group — Business Card Design Brief
Overview
Design a double-sided business card for Varnek Group that highlights our two service arms: Varnek Communications (telecommunications) and Varnek Energy (business energy solutions). The card should feel smart and stand out when handed to clients.

Objectives
Showcase our areas of specialty clearly.
Reflect the overall Varnek / Varnek Group brand while acknowledging both arms.
Explore using both logos (Communications + Energy) or one unified logo, depending on the design.

Deliverables
One double-sided business card design (front + back).

Content & Copy
Front (preferred): Logo: Varnek / Varnek Group
Descriptor: Business Communications | Business Energy
Back:My contact details and company details
Core products: Business Mobile • Telephony • Internet • Business Energy Solutions

Brand & Visual Direction
We have a group logo currently tailored more toward telecoms, plus a separate Varnek Energy logo.
Please explore layouts that use both logos or just one, whichever works best.
Color: I wouldn't mind seeing an option using our the Blue/Purple gradient from our website (varnek-example.co.uk), but also open to non-gradient approaches and other colours..

Overall look: Smart, modern, and distinctive.
Format & Print Specs
Double-sided business card format. (Use a standard size

Must-Haves
Front: Varnek wording or Varnek Group wording with atleast 1 logo also on front “Business Communications | Business Energy.”

Back: Contact + company details and core products.
A design that stands out while remaining professional.

Nice-to-Have Options
A gradient version using our site’s Blue/Purple gradient.
A non-gradient version.
A dual-logo treatment versus a single-logo treatment.

Thanks
Dominic

```html
<!DOCTYPE html>
<html lang="en">
<head>
<meta charset="UTF-8">
<title>Varnek Group Business Card</title>
<link href="https://fonts.googleapis.com/css2?family=Poppins:wght@500;600;700;800&display=swap" rel="stylesheet">
<style>
  :root {
    --bg: #2a2a2a;
    --purple: #8c10d4;
    --violet: #5b3cbc;
    --blue: #2b5ea9;
    --navy: #1f1c6e;
    --white: #ffffff;
    --logo-blue: #1b63d8;
    --logo-green: #4cb81f;
  }
  * { box-sizing: border-box; margin: 0; padding: 0; }
  html, body { width: 1200px; height: 800px; overflow: hidden; }
  body {
    background: var(--bg);
    font-family: "Poppins", sans-serif;
    color: var(--white);
    display: flex;
    align-items: center;
    justify-content: center;
    gap: 40px;
  }
  .card {
    width: 540px;
    height: 310px;
    border-radius: 16px;
    background: linear-gradient(100deg, var(--purple) 0%, var(--violet) 30%, var(--blue) 62%, var(--navy) 100%);
    box-shadow: 0 12px 30px rgba(0,0,0,0.45);
    position: relative;
    display: flex;
    flex-direction: column;
    align-items: center;
    justify-content: center;
  }
  .brand {
    display: flex;
    align-items: center;
    gap: 14px;
  }
  .brand-dot {
    border-radius: 50%;
    background: var(--logo-blue);
  }
  .brand-name {
    font-weight: 800;
    letter-spacing: 1px;
    line-height: 1;
  }
  .card-front .brand-dot { width: 62px; height: 62px; }
  .card-front .brand-name { font-size: 60px; }
  .descriptor {
    margin-top: 34px;
    font-size: 13px;
    font-weight: 600;
    letter-spacing: 0.6px;
    text-transform: uppercase;
  }
  .descriptor .divider { margin: 0 10px; }

  .card-back { justify-content: flex-start; padding-top: 44px; }
  .brand-row { display: flex; gap: 34px; }
  .card-back .brand { gap: 9px; }
  .card-back .brand-dot { width: 30px; height: 30px; }
  .brand-dot.energy { background: var(--logo-green); }
  .card-back .brand-name { font-size: 30px; }
  .contact-row {
    margin-top: 26px;
    display: flex;
    gap: 34px;
    font-size: 15px;
    font-weight: 600;
  }
  .contact-item { display: flex; align-items: center; gap: 9px; }
  .icon-box {
    width: 24px; height: 22px;
    background: var(--white);
    border-radius: 4px;
    display: flex; align-items: center; justify-content: center;
  }
  .products {
    margin-top: 22px;
    text-align: center;
    font-size: 14px;
    font-weight: 600;
    line-height: 1.35;
    text-transform: uppercase;
  }
  .address {
    margin-top: 22px;
    font-size: 13px;
    font-weight: 600;
  }
</style>
</head>
<body>
  <section class="card card-front">
    <div class="brand">
      <span class="brand-dot"></span>
      <span class="brand-name">VARNEK</span>
    </div>
    <p class="descriptor">Business Communications<span class="divider">|</span>Business Energy</p>
  </section>

  <section class="card card-back">
    <div class="brand-row">
      <div class="brand">
        <span class="brand-dot"></span>
        <span class="brand-name">VARNEK</span>
      </div>
      <div class="brand">
        <span class="brand-dot energy"></span>
        <span class="brand-name">VARNEK</span>
      </div>
    </div>
    <div class="contact-row">
      <div class="contact-item">
        <span class="icon-box">
          <svg width="14" height="14" viewBox="0 0 24 24" aria-hidden="true"><path fill="#6a3cc4" d="M6.6 10.8a15.2 15.2 0 0 0 6.6 6.6l2.2-2.2c.3-.3.7-.4 1-.2 1.1.4 2.3.6 3.6.6.6 0 1 .4 1 1V20c0 .6-.4 1-1 1A17 17 0 0 1 3 4c0-.6.4-1 1-1h3.5c.6 0 1 .4 1 1 0 1.3.2 2.5.6 3.6.1.3 0 .7-.2 1z"/></svg>
        </span>
        <span>+44 0161 555 0148</span>
      </div>
      <div class="contact-item">
        <span class="icon-box">
          <svg width="14" height="14" viewBox="0 0 24 24" aria-hidden="true"><g fill="none" stroke="#3a4fb0" stroke-width="2"><circle cx="12" cy="12" r="9"/><path d="M3 12h18M12 3c3 3 3 15 0 18M12 3c-3 3-3 15 0 18"/></g></svg>
        </span>
        <span>www.varnek-example.co.uk</span>
      </div>
    </div>
    <p class="products">Business Mobile • Telephony • Internet<br>• Business Energy Solutions</p>
    <p class="address">24 Alder Row, Marlow Cross, England, MX1 2QA</p>
  </section>
</body>
</html>
```